FLYERENTWURF  für Make up Ausbildung
FLYERENTWURF für Make up Ausbildung
Zielgruppe
friseure die sich weiterbilden wollen
Aufgabenstellung
zu entwerfen ist ein doppelseitiger flyer in A4, zweimal gefalten.
außenseite:
erste spalte/deckblatt:
das logo (im anhang)
schriftzug: mira beauty schule
eventuell bild kussmund, wenn rechte vorhanden.
zweite spalte/hinterseite:
zahlungsbedingungen (text wird noch beigefügt)
dritte spalte:
personenbild (anhang)
personenbeschreibung (text wird noch beigefügt)
innenseite:
text aus anhang

```html
<!DOCTYPE html>
<html lang="de">
<head>
<meta charset="utf-8">
<title>mira beauty schule – flyer</title>
<link href="https://fonts.googleapis.com/css2?family=Open+Sans:wght@300;400;600&display=swap" rel="stylesheet">
<style>
:root{
  --bg:#ece9e4;
  --ink:#0b0b0b;
  --panel:#121212;
  --text:#d9d9d9;
  --muted:#9a9a9a;
  --pink:#c2185b;
  --pink-soft:#e0508a;
  --grey-star:#8a8a8a;
}
*{box-sizing:border-box;margin:0;padding:0}
html,body{width:1200px;height:1200px;overflow:hidden;background:var(--bg)}
body{position:relative;font-family:"Open Sans",Arial,sans-serif;color:var(--text)}
.sheet{position:absolute;background:var(--ink);box-shadow:0 6px 18px rgba(0,0,0,.25)}
.outside{left:50px;top:56px;width:1010px;height:514px}
.inside{left:444px;top:610px;width:716px;height:510px;padding:26px 14px 0}
.abs{position:absolute}

/* outside – about panel */
.about-title{left:24px;top:28px;font-size:13px;font-weight:300;color:#fff;letter-spacing:.2px}
.portrait{left:24px;top:80px;width:62px;height:110px;background:linear-gradient(160deg,#6b5a52,#2a2522);border:2px solid var(--pink);border-radius:4px}
.portrait-bar{left:24px;top:196px;width:62px;height:3px;background:var(--pink)}
.stars{left:90px;top:120px}
.about-text{left:24px;top:270px;width:276px;font-size:6.6px;line-height:1.45;color:var(--text)}
.about-text p{margin-bottom:6px}
.divider{left:302px;top:0;width:3px;height:300px;background:linear-gradient(var(--pink),transparent)}
.gallery-img{left:336px;width:100px;border-radius:10px}
.g1{top:60px;height:104px;background:linear-gradient(135deg,#f4f0f1,#e35a8b 55%,#b71f56)}
.g2{top:188px;height:106px;background:linear-gradient(135deg,#f2f2f2,#bfa99c 60%,#3b2e2a)}
.g3{top:314px;height:110px;background:linear-gradient(160deg,#f7f2ef,#e7c9bc)}

/* outside – cover */
.cover-band{left:482px;top:0;width:44px;height:514px;background:linear-gradient(90deg,#3a0d1f,var(--pink) 60%,#8e1242)}
.cover-band-line{left:520px;top:0;width:3px;height:514px;background:var(--pink-soft)}
.cover-vertical{left:486px;top:500px;transform:rotate(-90deg);transform-origin:left top;white-space:nowrap;font-size:17px;font-weight:300;color:#fff;line-height:1.05}
.cover-vertical span{display:block;color:#f4b7cf;font-size:14px}
.cover-photo{left:530px;top:0;width:480px;height:370px;background:linear-gradient(160deg,#f6e9e3,#e8c3b3 45%,#b57a6a 80%,#ffffff)}
.cover-name{left:640px;top:412px;font-size:36px;font-weight:300;color:#fff;letter-spacing:.5px}
.cover-sub{left:680px;top:460px;font-size:8px;color:var(--muted)}
.cover-stars{left:880px;top:18px}

/* inside */
.courses{display:grid;grid-template-columns:repeat(3,1fr);gap:16px;height:100%}
.course{font-size:6.2px;line-height:1.45;color:var(--text)}
.course-head{display:flex;align-items:center;gap:8px;margin-bottom:10px}
.course-icon{width:32px;height:16px;border-radius:3px;background:linear-gradient(90deg,#c9a99d,#6b4a40)}
.course-title{font-size:13px;font-weight:300;color:#fff;white-space:nowrap}
.course-title small{font-size:6px;color:var(--muted)}
.label{color:var(--pink-soft);font-weight:600;margin:7px 0 3px}
.list li{list-style:none;padding-left:9px;position:relative}
.list li::before{content:"";position:absolute;left:0;top:2px;width:4px;height:4px;background:var(--pink)}
.dates td{padding:0 6px 0 0}
.dates td:first-child{padding-left:9px;position:relative}
.dates td:first-child::before{content:"";position:absolute;left:0;top:2px;width:4px;height:4px;background:var(--pink)}
.price{font-size:10px;color:#fff;margin-top:2px}
.price small{font-size:5px;color:var(--muted)}
.inside-bar{position:absolute;right:14px;bottom:66px;width:60px;height:3px;background:#fff}
</style>
</head>
<body>

<section class="sheet outside" aria-label="Außenseite">
  <h2 class="abs about-title">lena korbach</h2>
  <div class="abs portrait" role="img" aria-label="Porträtfoto der Trainerin"></div>
  <div class="abs portrait-bar"></div>
  <svg class="abs stars" width="60" height="50" viewBox="0 0 60 50" aria-hidden="true">
    <polygon fill="#6e6e6e" points="18,2 22,14 35,14 25,22 29,35 18,27 7,35 11,22 1,14 14,14"/>
    <polygon fill="#9a9a9a" points="42,8 46,20 58,20 48,27 52,40 42,32 32,40 36,27 26,20 38,20"/>
  </svg>
  <div class="abs about-text">
    <p>ich habe mich früh für den beruf friseur entschieden, weil ich schon immer freude daran hatte, menschen schöner zu machen. nach meiner ausbildung sammelte ich erfahrungen in salons, bei fotoshootings und auf der bühne. dabei entdeckte ich meine leidenschaft für make-up, das jeden look erst vollständig macht.</p>
    <p>am meisten gefällt mir an meiner arbeit die vielfalt. ich arbeite mit modellen, bräuten und schauspielern und lerne jeden tag neue techniken kennen. diese erfahrung gebe ich heute gerne an friseure weiter, die ihr können erweitern möchten.</p>
    <p>auf meine kurse freue ich mich besonders, weil ich dort sehe, wie schnell kreative friseure neue ideen umsetzen. in kleinen gruppen arbeiten wir praxisnah, persönlich und mit hochwertigen produkten, damit jeder teilnehmer mit sicherheit und eigenem stil in den salon zurückkehrt.</p>
  </div>
  <div class="abs divider"></div>
  <div class="abs gallery-img g1" role="img" aria-label="Foto von Make-up-Pinsel und Lippenstift"></div>
  <div class="abs gallery-img g2" role="img" aria-label="Foto einer Frau beim Schminken"></div>
  <div class="abs gallery-img g3" role="img" aria-label="Foto von Kinn und Hals eines Modells"></div>

  <div class="abs cover-band"></div>
  <div class="abs cover-band-line"></div>
  <div class="abs cover-vertical">mira<span>beauty schule</span></div>
  <div class="abs cover-photo" role="img" aria-label="Großes Beauty-Porträtfoto"></div>
  <svg class="abs cover-stars" width="120" height="70" viewBox="0 0 120 70" aria-hidden="true">
    <polygon fill="rgba(255,255,255,.55)" points="40,4 47,24 68,24 51,36 57,56 40,44 23,56 29,36 12,24 33,24"/>
    <polygon fill="rgba(255,255,255,.35)" points="90,2 95,16 110,16 98,25 102,39 90,30 78,39 82,25 70,16 85,16"/>
  </svg>
  <div class="abs cover-name">mira beauty schule</div>
  <div class="abs cover-sub">make-up ausbildung für friseure</div>
</section>

<section class="sheet inside" aria-label="Innenseite">
  <div class="courses">
    <article class="course">
      <div class="course-head"><div class="course-icon" role="img" aria-label="Detailfoto Augen-Make-up"></div><h3 class="course-title">basic education <small>teil 1</small></h3></div>
      <p>in diesem workshop lernst du die grundlagen des professionellen make-ups. wir zeigen dir, wie du hauttypen erkennst, die passenden produkte wählst und einen natürlichen look sicher umsetzt.</p>
      <p class="label">inhalte auf einen blick</p>
      <ul class="list">
        <li>produktwissen</li><li>gesichtsanalyse</li><li>optimierung der gesichtsformen</li><li>augenmakeup</li><li>makeup für verschiedene anlässe</li><li>augenbrauen richtig formen</li><li>tages-makeup</li><li>abend-makeup</li><li>spezial-makeup</li>
      </ul>
      <p class="label">termine</p>
      <table class="dates"><tbody>
        <tr><td>mo.</td><td>04.08.2011</td><td>10-18 uhr</td></tr>
        <tr><td>mo.</td><td>08.08.2011</td><td>10-18 uhr</td></tr>
        <tr><td>mo.</td><td>15.08.2011</td><td>10-18 uhr</td></tr>
        <tr><td>mo.</td><td>22.08.2011</td><td>10-18 uhr</td></tr>
        <tr><td>mo.</td><td>29.08.2011</td><td>10-18 uhr</td></tr>
        <tr><td>mo.</td><td>05.09.2011</td><td>10-18 uhr</td></tr>
        <tr><td>mo.</td><td>12.09.2011</td><td>10-18 uhr</td></tr>
      </tbody></table>
      <p class="label">voraussetzungen</p>
      <p>dieser kurs ist geeignet für einsteiger und friseure, die ihr angebot um professionelles make-up erweitern möchten.</p>
      <p class="label">kosten</p>
      <p class="price">€ 990 <small>inkl. mwst</small></p>
      <p class="label">anmeldung</p>
      <p>bis 01.08.2011 &nbsp; kasse@lockenglanzsalon.example oder unter 0 4417 88 20</p>
    </article>

    <article class="course">
      <div class="course-head"><div class="course-icon" role="img" aria-label="Detailfoto geschminkte Lippen"></div><h3 class="course-title">junior make up artist <small>teil 2</small></h3></div>
      <p>junior make up artists, die ihren basic-kurs bereits absolviert haben, vertiefen hier ihr wissen. im mittelpunkt stehen foto-, braut- und bühnen-makeup sowie das sichere arbeiten unter zeitdruck.</p>
      <p class="label">inhalte auf einen blick</p>
      <ul class="list">
        <li>braut</li><li>anti-aging-makeup</li><li>foto-makeup</li><li>schwarz/weiß-foto-makeup</li><li>männer-makeup</li><li>typberatung</li><li>make-up-trends</li><li>brush-makeup</li>
      </ul>
      <p class="label">termine</p>
      <table class="dates"><tbody>
        <tr><td>mo.</td><td>10.07.2011</td><td>10-18 uhr</td></tr>
        <tr><td>mo.</td><td>17.07.2011</td><td>10-18 uhr</td></tr>
        <tr><td>mo.</td><td>24.07.2011</td><td>10-18 uhr</td></tr>
        <tr><td>mo.</td><td>31.07.2011</td><td>10-18 uhr</td></tr>
        <tr><td>mo.</td><td>07.08.2011</td><td>10-18 uhr</td></tr>
        <tr><td>mo.</td><td>14.08.2011</td><td>10-18 uhr</td></tr>
        <tr><td>mo.</td><td>21.08.2011</td><td>10-18 uhr</td></tr>
        <tr><td>mo.</td><td>28.08.2011</td><td>10-18 uhr</td></tr>
      </tbody></table>
      <p class="label">voraussetzungen</p>
      <p>dieser kurs ist geeignet für friseure mit basiswissen. teilnehmer sollten den ersten kurs abgeschlossen haben oder gleichwertige praxis nachweisen können.</p>
      <p class="label">kosten</p>
      <p class="price">€ 990 <small>inkl. mwst</small></p>
      <p class="label">anmeldung</p>
      <p>bis 01.07.2011 &nbsp; kasse@lockenglanzsalon.example oder unter 0 4417 88 20</p>
    </article>

    <article class="course">
      <div class="course-head"><div class="course-icon" role="img" aria-label="Detailfoto Make-up-Produkte"></div><h3 class="course-title">senior make up artist <small>teil 3</small></h3></div>
      <p>in der abschlussstufe lernst du, kreative looks für mode, werbung und bühne selbstständig zu entwickeln. du arbeitest mit profis, planst eigene shootings und baust dein portfolio auf.</p>
      <p class="label">inhalte auf einen blick</p>
      <ul class="list">
        <li>spezialeffekt-makeup</li><li>verschiedene kulturen und epochen</li><li>geschichte des makeup</li><li>laufsteg-makeup</li><li>e-mail-makeup planung</li>
      </ul>
      <p class="label">termine</p>
      <table class="dates"><tbody>
        <tr><td>mo.</td><td>11.09.2011</td><td>10-18 uhr</td></tr>
        <tr><td>mo.</td><td>18.09.2011</td><td>10-18 uhr</td></tr>
        <tr><td>mo.</td><td>25.09.2011</td><td>10-18 uhr</td></tr>
        <tr><td>mo.</td><td>02.10.2011</td><td>10-18 uhr</td></tr>
        <tr><td>mo.</td><td>09.10.2011</td><td>10-18 uhr</td></tr>
        <tr><td>mo.</td><td>16.10.2011</td><td>10-18 uhr</td></tr>
        <tr><td>mo.</td><td>23.10.2011</td><td>10-18 uhr</td></tr>
        <tr><td>mo.</td><td>30.10.2011</td><td>10-18 uhr</td></tr>
      </tbody></table>
      <p class="label">voraussetzungen</p>
      <p>dieser kurs ist geeignet für kreative friseure mit erfahrung, die beide vorherigen stufen abgeschlossen haben und eigene projekte verwirklichen wollen.</p>
      <p class="label">kosten</p>
      <p class="price">€ 990 <small>inkl. mwst</small></p>
      <p class="label">anmeldung</p>
      <p>bis 01.09.2011 &nbsp; kasse@lockenglanzsalon.example oder unter 0 4417 88 20. bei anmeldung für alle drei kurse erhältst du einen rabatt.</p>
    </article>
  </div>
  <div class="inside-bar"></div>
</section>

</body>
</html>
```